Birchford Realty Business Card

Business Card:

Somewhere on front of card, please include Broker License Number: 5839162

Website is BirchfordRealty.example

Address is:
7218 Crestover Ave E
Larkmoor, OH 48271

I'll let you use creative freedom on the rest; we obviously need Name, Title, Email (@BirchfordRealty.example), Office Phone, Cell Phone.

Don't want any special die-cutting, just a standard size business card.

On the back, include a place for the date and time of an appointment to be written in pen.

Requirements
Must have
• Our logo, attached to email.

```html
<!DOCTYPE html>
<html lang="en">
<head>
<meta charset="utf-8">
<title>Birchford Realty – Business Card</title>
<link href="https://fonts.googleapis.com/css2?family=Open+Sans:wght@400;600;700&display=swap" rel="stylesheet">
<style>
  :root {
    --navy: #25236b;
    --white: #ffffff;
    --silver-light: #f1f2f4;
    --silver-mid: #b9bcc2;
    --silver-dark: #8d9097;
    --grey-text: #7b7e85;
    --stage: #e9e6e1;
  }
  * { box-sizing: border-box; margin: 0; padding: 0; }
  html, body { width: 1200px; height: 784px; overflow: hidden; }
  body {
    background: var(--stage);
    font-family: "Open Sans", Arial, sans-serif;
    position: relative;
  }
  .card {
    position: absolute;
    width: 550px;
    height: 314px;
    overflow: hidden;
    box-shadow: 0 6px 18px rgba(0,0,0,0.18);
  }
  .card-back { left: 40px; top: 235px; background: var(--navy); }
  .card-front { left: 610px; top: 235px; background: var(--white); }

  .card-art { position: absolute; inset: 0; width: 100%; height: 100%; }

  /* Back */
  .back-wordmark {
    position: absolute; left: 0; right: 0; top: 66px;
    text-align: center;
    font-size: 34px; font-weight: 700; letter-spacing: 0.5px;
    color: var(--silver-mid);
    white-space: nowrap;
  }
  .appointment-row, .schedule-row {
    position: absolute; display: flex; align-items: center;
    color: var(--white); font-size: 11px; font-weight: 600; letter-spacing: 0.5px;
    white-space: nowrap;
  }
  .appointment-row { left: 0; right: 24px; top: 156px; justify-content: flex-end; gap: 10px; }
  .schedule-row { left: 24px; right: 24px; top: 214px; gap: 10px; }
  .write-field { display: block; height: 20px; background: var(--white); box-shadow: inset 0 0 0 1px var(--silver-mid); }
  .appointment-row .write-field { width: 230px; }
  .schedule-row .field-date { width: 210px; }
  .schedule-row .field-time { width: 170px; }
  .schedule-row .label-time { margin-left: 12px; }

  /* Front */
  .holder { position: absolute; right: 26px; top: 20px; text-align: right; }
  .holder-name { font-size: 16px; font-weight: 600; color: var(--navy); }
  .holder-title { font-size: 9px; color: var(--grey-text); margin-top: -2px; }
  .front-wordmark {
    position: absolute; left: 40px; top: 92px;
    font-size: 38px; font-weight: 700; color: var(--navy); letter-spacing: 0.3px;
    white-space: nowrap;
  }
  .contact-list {
    position: absolute; left: 24px; top: 206px; list-style: none;
    color: var(--white); font-size: 12.5px; line-height: 15px;
    white-space: nowrap;
  }
  .contact-list li { display: flex; align-items: center; gap: 7px; }
  .contact-list .icon { width: 12px; height: 12px; flex: none; }
  .contact-list .indent { padding-left: 19px; }
  .license {
    position: absolute; left: 43px; top: 297px;
    color: var(--white); font-size: 8.5px; line-height: 11px; white-space: nowrap;
  }
</style>
</head>
<body>

<section class="card card-back" aria-label="Back of business card">
  <svg class="card-art" viewBox="0 0 550 314" aria-hidden="true">
    <rect width="550" height="314" fill="var(--navy)"/>
  </svg>
  <div class="back-wordmark">Birchford Realty</div>
  <div class="appointment-row">
    <span class="label-appointment">APPOINTMENT</span>
    <span class="write-field"></span>
  </div>
  <div class="schedule-row">
    <span class="label-date">DATE:</span>
    <span class="write-field field-date"></span>
    <span class="label-time">TIME:</span>
    <span class="write-field field-time"></span>
  </div>
</section>

<section class="card card-front" aria-label="Front of business card">
  <svg class="card-art" viewBox="0 0 550 314" aria-hidden="true">
    <defs>
      <linearGradient id="silverBand" x1="0" y1="0" x2="1" y2="0">
        <stop offset="0" stop-color="var(--silver-dark)"/>
        <stop offset="0.35" stop-color="var(--silver-light)"/>
        <stop offset="0.7" stop-color="var(--silver-mid)"/>
        <stop offset="1" stop-color="var(--silver-light)"/>
      </linearGradient>
    </defs>
    <rect width="550" height="314" fill="var(--white)"/>
    <polygon points="0,200 550,150 550,314 0,314" fill="var(--navy)"/>
    <polygon points="0,188 550,138 550,150 0,200" fill="url(#silverBand)"/>
  </svg>

  <div class="holder">
    <div class="holder-name">Dana Whitcombe</div>
    <div class="holder-title">Manager</div>
  </div>

  <div class="front-wordmark">Birchford Realty</div>

  <ul class="contact-list">
    <li>
      <svg class="icon" viewBox="0 0 12 12" aria-hidden="true"><rect x="3" y="0.5" width="6" height="11" rx="1" fill="none" stroke="#fff"/><line x1="5" y1="9.5" x2="7" y2="9.5" stroke="#fff"/></svg>
      517.555.0148
    </li>
    <li>
      <svg class="icon" viewBox="0 0 12 12" aria-hidden="true"><path d="M2.5 1 L4.5 1 L5.3 3.6 L4 4.6 C4.7 6.1 5.9 7.3 7.4 8 L8.4 6.7 L11 7.5 L11 9.5 C11 10.3 10.3 11 9.5 11 C5 11 1 7 1 2.5 C1 1.7 1.7 1 2.5 1 Z" fill="#fff"/></svg>
      888.555.0192 Ext. 4
    </li>
    <li>
      <svg class="icon" viewBox="0 0 12 12" aria-hidden="true"><rect x="0.5" y="2" width="11" height="8" fill="none" stroke="#fff"/><polyline points="0.5,2 6,6.5 11.5,2" fill="none" stroke="#fff"/></svg>
      Dana@BirchfordRealty.example
    </li>
    <li>
      <svg class="icon" viewBox="0 0 12 12" aria-hidden="true"><circle cx="6" cy="6" r="5.3" fill="none" stroke="#fff"/><ellipse cx="6" cy="6" rx="2.3" ry="5.3" fill="none" stroke="#fff"/><line x1="0.7" y1="6" x2="11.3" y2="6" stroke="#fff"/></svg>
      www.BirchfordRealty.example
    </li>
    <li>
      <svg class="icon" viewBox="0 0 12 12" aria-hidden="true"><polygon points="6,0.8 11.5,5.8 10,5.8 10,11 7.3,11 7.3,7.8 4.7,7.8 4.7,11 2,11 2,5.8 0.5,5.8" fill="#fff"/></svg>
      7218 Crestover Ave E
    </li>
    <li class="indent">Larkmoor, OH 48271</li>
  </ul>
  <div class="license">Broker License Number: 5839162</div>
</section>

</body>
</html>
```